Small chamber of commerce in upstate new york. Need basic design to announce a new chocolate festival that will intend to bring in tourists to our area and give our local merchants exposure.

Industry/Entity Type

Chamber Of Commerce

Requirements
Must have
• (Beyond the information that has been listed on the enclosed jpeg, I would like to have some details on the reverse side that would include:)

Cooking with Chocolate Demo
Chocolate Decorating competition with Kids/Pastry Chefs
Live Music
Fudge Rocket Scooter Sprint
Lots & Lots of Chocolate!!!

More information contact info@pinevalechamber.org or call 845.555.0147.

```html
<!DOCTYPE html>
<html lang="en">
<head>
<meta charset="utf-8">
<title>Pinevale Chocolate Festival – Flyer</title>
<link rel="stylesheet" href="https://fonts.googleapis.com/css2?family=Lobster&family=Oswald:wght@500;700&display=swap">
<style>
  :root {
    --bg: #efeae2;
    --cream: #f3eddc;
    --cream-soft: #e4dcc6;
    --cocoa-dark: #3b2f25;
    --cocoa: #4e4133;
    --cocoa-mid: #6b5c4b;
    --mauve: #a38b88;
    --shadow: rgba(40, 28, 18, 0.35);
  }
  * { margin: 0; padding: 0; box-sizing: border-box; }
  html, body { width: 1200px; height: 1175px; overflow: hidden; background: var(--bg); }
  .canvas { position: relative; width: 1200px; height: 1175px; }

  .card {
    position: absolute;
    overflow: hidden;
    box-shadow: 6px 8px 18px var(--shadow);
  }

  /* Front */
  .card--front {
    left: 60px; top: 70px; width: 480px; height: 630px;
    background: var(--cream);
    border: 10px solid #fbf8f1;
  }
  .card--front svg { position: absolute; inset: 0; }
  .front-title {
    position: absolute; left: 36px; top: 26px;
    font-family: "Lobster", cursive;
    color: var(--cocoa);
    line-height: 0.9;
    transform: rotate(-6deg);
    transform-origin: left top;
  }
  .front-title .line-1 { display: block; font-size: 86px; }
  .front-title .line-2 { display: block; font-size: 62px; margin-left: 170px; }

  .front-info {
    position: absolute; left: 170px; top: 430px; width: 280px;
    font-family: "Oswald", sans-serif; color: var(--cream);
    text-align: center;
  }
  .front-info .org { font-size: 20px; font-weight: 700; letter-spacing: 1.5px; text-align: left; padding-left: 28px; }
  .front-info .org span { font-size: 26px; }
  .front-info .org small { display: block; font-size: 12px; letter-spacing: 0.5px; margin-top: -4px; }
  .front-info .date { font-size: 26px; font-weight: 700; margin-top: 14px; }
  .front-info .web { font-size: 16px; font-weight: 700; margin-top: 18px; letter-spacing: 0.5px; }

  /* Back */
  .card--back {
    left: 620px; top: 470px; width: 520px; height: 640px;
    border: 8px solid var(--cocoa-dark);
  }
  .card--back .swirl { position: absolute; inset: 0; }
  .events {
    position: absolute; left: 78px; top: 140px; width: 390px; height: 320px;
    background: var(--cocoa-dark);
    border: 12px solid var(--cream-soft);
    box-shadow: 4px 6px 10px var(--shadow);
    transform: rotate(5deg);
    font-family: "Oswald", sans-serif; color: var(--cream);
    text-align: center;
    padding: 34px 20px 0;
  }
  .events li { list-style: none; font-size: 18px; font-weight: 500; line-height: 1.35; margin-bottom: 14px; }
  .events li.finale { font-size: 26px; font-weight: 700; margin-top: 8px; }
  .events .topper {
    position: absolute; right: -8px; top: -40px; width: 56px; height: 56px;
    background: var(--cream); border-radius: 50% 50% 40% 40%;
  }
  .contact {
    position: absolute; left: 0; right: 0; bottom: 34px;
    font-family: "Oswald", sans-serif; font-size: 12px; color: var(--cream);
    text-align: center; line-height: 1.4;
  }
</style>
</head>
<body>
<div class="canvas">

  <section class="card card--front">
    <svg width="460" height="610" viewBox="0 0 460 610">
      <defs>
        <radialGradient id="swirl-front" cx="0.5" cy="0.5" r="0.6">
          <stop offset="0" stop-color="#d9cfb8"/>
          <stop offset="0.5" stop-color="#8a7a66"/>
          <stop offset="1" stop-color="#4e4133"/>
        </radialGradient>
      </defs>
      <path role="img" aria-label="Radiating chocolate and cream swirl pattern"
            d="M0 290 C 120 210, 260 170, 460 150 L460 610 L0 610 Z" fill="url(#swirl-front)"/>
      <path d="M0 300 C 120 220, 260 180, 460 160" fill="none" stroke="#fbf8f1" stroke-width="5"/>
      <path class="info-cloud" d="M60 610 L60 470 Q 60 400 150 395 L 400 380 Q 460 378 460 430 L460 610 Z" fill="#3b2f25"/>
      <rect role="img" aria-label="Soft-serve chocolate swirl icon" x="390" y="350" width="44" height="44" rx="22" fill="#f3eddc"/>
    </svg>
    <h1 class="front-title"><span class="line-1">Chocolate</span><span class="line-2">festival</span></h1>
    <div class="front-info">
      <p class="org">PINEVALE <span>&amp;</span><small>THE CHOCOLATE FESTIVAL</small></p>
      <p class="date">Coming Nov 1, 2014</p>
      <p class="web">www.pinevalechamber.org</p>
    </div>
  </section>

  <section class="card card--back">
    <svg class="swirl" width="504" height="624" viewBox="0 0 504 624" role="img" aria-label="Radiating chocolate, cream and mauve swirl pattern">
      <defs>
        <radialGradient id="swirl-back" cx="0.55" cy="0.4" r="0.75">
          <stop offset="0" stop-color="#e4dcc6"/>
          <stop offset="0.35" stop-color="#a38b88"/>
          <stop offset="0.7" stop-color="#5a4a3b"/>
          <stop offset="1" stop-color="#3b2f25"/>
        </radialGradient>
      </defs>
      <rect width="504" height="624" fill="url(#swirl-back)"/>
    </svg>
    <div class="events">
      <span class="topper" role="img" aria-label="Soft-serve chocolate swirl icon"></span>
      <ul>
        <li>Cooking with Chocolate Demo</li>
        <li>Chocolate Decorating competition<br>with Kids/Pastry Chefs</li>
        <li>Live Music</li>
        <li>Fudge Rocket Scooter Sprint</li>
        <li class="finale">Lots &amp; Lots of Chocolate!!!</li>
      </ul>
    </div>
    <p class="contact">More information contact info@pinevalechamber.org<br>or call 845.555.0147</p>
  </section>

</div>
</body>
</html>
```